Website Design for Business Law Firm

We have a logo and now we would like a web site design for our new website. Our small firm provides creative and aggressive transactional (not litigation) legal services to advise healthcare, technology, internet-based and traditional companies and investors in such companies on healthcare, technology, financing, mergers/acquisitions, real estate and other transactions, legal compliance and general corporate and business matters.

We would like to see a website design that is professional and appropriate for executives, professionals, investors and government regulators to visit, that conveys professionalism and competence while being a little edgy and modern - no typical legal motifs such as gavels, books, or scales of justice. We advise businesses and investors and guide them through complicated issues quickly, capably and differently from other law firms. We are part of the business team and get things done.

The logo is attached, and we like gray as a color to complement it. The intention of the logo is to convey that in a storm or challenging time, people come to this firm, and people come to this firm when they need the power and disruption to change things or shake them up.

I have also enclosed a picture of our business card for consideration.

On the other hand, you can check out the current simple site at www.venhollow.example to see we have used a space motif in the past to evoke that we help create stars (the nebula featured there). This is not a necessary part of the new website and it may look better without it.

We appreciate your creativity and look forward to designs.

Industry/Entity Type

Business

Requirements
Must have
• We anticipate the following pages, and you may submit different ideas for the different pages:
• 1. Landing page
• 2. Services pages - healthcare, IT/Technology, general counsel services, financings, mergers/acquisitions, mediation/arbitration, procurement and productization
• 3. About Us including contact information
• Our name and contact information:
• Quellane Law Firm, P.C.
• 8716 SW 19th Ave.
• Portland, OR 97213
• phone: 971.555.0143
• fax: 971.555.0187
Nice to have
• Please consider designs that enhance the impressions we are looking for
Should not have
• Please no gavels, scales of justice, law books, or similar traditional legal imagery.

```html
<!DOCTYPE html>
<html lang="en">
<head>
<meta charset="utf-8">
<title>Quellane Law Firm</title>
<link rel="stylesheet" href="https://fonts.googleapis.com/css2?family=Open+Sans:wght@400;600&family=PT+Sans:wght@400;700&display=swap">
<style>
:root{
  --bronze:#7b6b4f;
  --bronze-dark:#5f523b;
  --header-tint:rgba(72,60,40,.82);
  --cream:#f4efe3;
  --ink:#141210;
  --teal:#4d696c;
  --grey-text:#9a9a9a;
  --white:#ffffff;
}
*{margin:0;padding:0;box-sizing:border-box}
html,body{width:1120px;height:1200px;overflow:hidden}
body{position:relative;background:var(--white);font-family:"Open Sans",Arial,sans-serif;color:var(--cream)}
.abs{position:absolute}

/* hero */
.hero{left:0;top:0;width:1120px;height:533px;
  background:linear-gradient(100deg,#5b4a2c 0%,#a08a55 28%,#c9b77c 50%,#8a7447 72%,#4a3d26 100%)}
.hero-shade{left:0;top:0;width:1120px;height:533px;
  background:linear-gradient(180deg,rgba(0,0,0,0) 55%,rgba(40,30,15,.45) 100%)}
.site-header{left:0;top:0;width:1120px;height:108px;background:var(--header-tint)}
.brand{left:196px;top:14px;width:272px;text-align:center;font-family:"PT Sans",sans-serif;color:var(--white)}
.brand-name{font-size:40px;letter-spacing:7px;line-height:54px;font-weight:400}
.brand-sub{font-size:18px;letter-spacing:5px;line-height:24px;font-weight:400}
.account-nav{left:740px;top:8px;width:213px;height:30px;background:rgba(60,50,34,.75);
  display:flex;gap:15px;align-items:center;justify-content:center;font-size:13px;color:var(--cream)}
.header-contact{left:760px;top:44px;font-size:20px;line-height:27px;color:var(--white)}
.header-contact div{display:flex;align-items:center;gap:10px}
.headline{left:208px;top:164px;font-family:"PT Sans",sans-serif;font-weight:700;font-size:42px;
  line-height:50px;color:var(--white);text-transform:uppercase;text-shadow:1px 2px 3px rgba(0,0,0,.35)}
.slider-dots{left:478px;top:533px;display:flex;gap:5px}
.slider-dots span{width:51px;height:5px;background:#2c261c}
.slider-dots span.active{background:#ece6d6}

/* services */
.services{left:0;top:533px;width:1120px;height:387px;background:var(--bronze)}
.services-title{left:203px;top:550px;font-family:"PT Sans",sans-serif;font-weight:700;font-size:29px;color:var(--ink)}
.service-list{list-style:none;font-size:13px;line-height:16px;color:var(--cream)}
.service-list li{position:absolute;left:24px;width:220px;white-space:nowrap}
.service-list li::before{content:"»";position:absolute;left:-24px;top:-2px;font-size:18px;color:#2a241a}
.col-left{left:200px;top:0}
.col-right{left:445px;top:0}
.advisor-photo{left:740px;top:540px;width:180px;height:380px;
  background:linear-gradient(180deg,rgba(122,107,79,0) 0%,rgba(60,52,44,.55) 40%,rgba(25,23,22,.8) 100%);
  border-radius:90px 90px 0 0}

/* intro */
.intro-title{left:199px;top:946px;font-family:"PT Sans",sans-serif;font-weight:700;font-size:26px;letter-spacing:1px;color:var(--ink)}
.intro-title span{color:var(--teal)}
.lorem{font-size:10.5px;line-height:14.5px;color:var(--grey-text)}
.btn{display:flex;align-items:center;justify-content:center;background:var(--bronze);color:var(--white);font-size:13px}
.divider{left:694px;top:952px;width:1px;height:130px;background:#e2e2e2}
.testimonials-title{left:711px;top:946px;font-family:"PT Sans",sans-serif;font-weight:700;font-size:26px;letter-spacing:1px;color:var(--teal)}

/* footer */
.site-footer{left:0;top:1110px;width:1120px;height:90px;background:var(--bronze)}
.foot-text{font-family:"PT Sans",sans-serif;font-size:15px;line-height:20px;color:var(--white)}
.copyright{left:0;top:1177px;width:1120px;text-align:center;font-family:"PT Sans",sans-serif;font-size:12px;color:var(--cream)}
</style>
</head>
<body>

<div class="abs hero" role="img" aria-label="Sepia-toned photograph of a courtroom interior with benches and windows"></div>
<div class="abs hero-shade"></div>

<header class="abs site-header"></header>
<div class="abs brand">
  <div class="brand-name">QUELLANE</div>
  <div class="brand-sub">LAW FIRM</div>
</div>
<nav class="abs account-nav"><span>For lawyers</span><span>Sign in</span><span>Register</span></nav>
<div class="abs header-contact">
  <div><svg width="14" height="18" viewBox="0 0 14 18"><path d="M3 1 L6 5 L4 7 Q5 11 8 13 L10 11 L13 14 L10 17 Q3 14 1 5 Z" fill="#fff"/></svg>Tel: 971.555.0143</div>
  <div><svg width="16" height="14" viewBox="0 0 16 14"><rect x="1" y="5" width="14" height="7" rx="1" fill="#fff"/><rect x="4" y="1" width="8" height="5" fill="#ddd"/></svg>fax: 971.555.0187</div>
</div>

<h1 class="abs headline">Pragmatic,<br>Creative<br>Services for<br>Innovative<br>Businesses</h1>
<div class="abs slider-dots"><span></span><span class="active"></span><span></span></div>

<section class="abs services"></section>
<div class="abs advisor-photo" role="img" aria-label="Photograph of a smiling attorney in a vest and skirt gesturing toward the service list"></div>
<h2 class="abs services-title">WHAT WE DO</h2>
<ul class="abs service-list col-left">
  <li style="top:590px">Stragtegic Alliances</li>
  <li style="top:625px">Vandor Management</li>
  <li style="top:658px">Venture Financing</li>
  <li style="top:695px">Contracts</li>
  <li style="top:732px">Mergers and Acquisitions</li>
  <li style="top:769px">Service as a Mediator or Arbitrator</li>
  <li style="top:803px">Creative Private Financing<br>Arrangements</li>
  <li style="top:855px">Audits,Analyses and legal project<br>management</li>
</ul>
<ul class="abs service-list col-right">
  <li style="top:590px">Outsourcing</li>
  <li style="top:621px">Real Estate</li>
  <li style="top:658px">Dispute Resolution</li>
  <li style="top:695px">Businesses Relationships</li>
  <li style="top:732px">Venture Formation and startup</li>
  <li style="top:769px">Procurements-Buying or selling</li>
  <li style="top:804px">Licensing and Technology<br>Exploitation</li>
  <li style="top:854px">Local Counsel for Transactions<br>and dueDiligence</li>
</ul>

<h2 class="abs intro-title">WELLCOME TO <span>QUELLANE LAW FIRM</span></h2>
<p class="abs lorem" style="left:199px;top:982px;width:490px">Lorem ipsum dolor sit amet, consectetuer adipiscing elit, sed diam nonummy nibh euismod tincidunt laoreet dolore magna aliquam erat volutpat. Ut wisi enim ad minim veniam, quis nostrud exerci tation ullamcorper suscipit lobortis nisl ut aliquip ex ea commodo consequat. Duis autem vel eum iriure dolor in hendrerit in vulputate velit esse molestie consequat,</p>
<a class="abs btn" style="left:198px;top:1051px;width:78px;height:23px">Read more</a>
<div class="abs divider"></div>
<h2 class="abs testimonials-title">TESTIMONIALS</h2>
<p class="abs lorem" style="left:711px;top:982px;width:210px">Lorem ipsum dolor sit amet, consectetuer adipiscing elit, sed nonummy nibh euismod tincidunt laoreet dolore magna aliquam erat volutpat.</p>
<a class="abs btn" style="left:711px;top:1052px;width:92px;height:24px">Read more</a>

<footer class="abs site-footer"></footer>
<div class="abs foot-text" style="left:178px;top:1120px;display:flex;align-items:center;gap:8px">
  <svg width="16" height="12" viewBox="0 0 16 12"><rect x="0.5" y="0.5" width="15" height="11" fill="none" stroke="#fff"/><path d="M1 1 L8 7 L15 1" fill="none" stroke="#fff"/></svg>info@quellane.example</div>
<svg class="abs" style="left:444px;top:1120px" width="16" height="20" viewBox="0 0 16 20"><path d="M8 19 C3 12 1 9 1 7 A7 7 0 0 1 15 7 C15 9 13 12 8 19 Z" fill="none" stroke="#fff" stroke-width="1.4"/><circle cx="8" cy="7" r="2.5" fill="none" stroke="#fff" stroke-width="1.4"/></svg>
<div class="abs foot-text" style="left:471px;top:1121px;letter-spacing:.5px">Quellane Law Firm, P.C.<br>P.O. Box 5521, Portland, OR 97299</div>
<div class="abs foot-text" style="left:806px;top:1118px">
  <div style="display:flex;align-items:center;gap:5px"><svg width="14" height="12" viewBox="0 0 14 12"><path d="M1 4 Q7 -1 13 4 L11 6 L9 4 L5 4 L3 6 Z" fill="#fff"/><rect x="3" y="6" width="8" height="5" fill="#fff"/></svg>Tel: 971.555.0143</div>
  <div style="display:flex;align-items:center;gap:5px;margin-top:4px"><svg width="14" height="12" viewBox="0 0 14 12"><rect x="1" y="4" width="12" height="7" rx="1" fill="#fff"/><rect x="3" y="1" width="8" height="4" fill="#ddd"/></svg>fax: 971.555.0187</div>
</div>
<p class="abs copyright">Copyright © 2013 Quellane Law Firm, P.C. All rights reserved.</p>

</body>
</html>
```